Prime Care Company - Inside Back Cover of KESTO Magazine Ad -

We need a full page ad that can also be expanded into a full two page - For Prime Care Residential Services Company - QNV Cleaning is the Largest in the country (UAE) Hurra Mendo, (Maintenance, Pest Control, AC Duct Cleaning and Remodeling)

Please see all logos attached
There are two pervious fliers for EXAMPLE ONLY - do NOT want something that looks the same - want new & fresh!

Target Market(s)

Families, Airport Lounges, Hotels and Airline travelers will all view this Magazine.

Industry/Entity Type

Residential

Font styles to use
Serif

Colors

Designer to choose colors to be used in the design.

Requirements
Must have
• Sizes
• Double Page Spread Advert
• (DPS) 265mm (h) x 448mm (w)
• Full Page Specs:
• Ø Trim W200 x H265 mm
• Ø Bleed W210 x H275 mm
• Ø Type W195 x H250 mm
• Bleed
• Artwork for all adverts must include a 5mm bleed on all sides (see sizes above), all text and images should be at least a further 5mm from the crop guides. The easiest way of thinking of this if you are uncertain is to ensure the
• background image goes to right to the edge of the file and then all text, logos, etc are at least 8mm from the edges. To ensure correct printing an appropriate border will be added to all artwork supplied without correct bleeds.
• Colour
• Artwork should be completed and saved in CMYK process, Please delete all unused colour swatches from the colour palettes. Do not use Pantone or similar colours
Nice to have
• Clean - easy to read -
• Bright Colors
• Should be different

```html
<!DOCTYPE html>
<html lang="en">
<head>
<meta charset="utf-8">
<title>QNV Cleaning – Double Page Spread</title>
<link href="https://fonts.googleapis.com/css2?family=Crimson+Text:wght@400;600;700&family=Oswald:wght@600&display=swap" rel="stylesheet">
<style>
  :root{
    --backdrop:#9a9a9a;
    --brand-blue:#1f6db4;
    --bar-blue:#1f72b8;
    --panel-top:#ffffff;
    --panel-bottom:#7f9fd6;
    --magenta:#bf2a85;
    --label-yellow:#f7c21b;
    --ink:#141414;
    --red:#b3241f;
    --navy:#1c2f5e;
  }
  *{margin:0;padding:0;box-sizing:border-box}
  html,body{width:1200px;height:1200px;overflow:hidden;background:var(--backdrop)}
  .spread{
    position:absolute;left:0;top:244px;width:1350px;height:800px;
    transform:scale(.8889);transform-origin:0 0;
    font-family:"Crimson Text",serif;color:var(--ink);overflow:hidden;
  }
  .spread-art{position:absolute;inset:0}
  .abs{position:absolute}
  .brand{left:70px;top:48px;display:flex;align-items:center;gap:12px}
  .brand-mark{width:38px;height:38px;border-radius:50%;background:var(--navy)}
  .brand-name{font-size:36px;font-weight:600;color:var(--navy);letter-spacing:1px;white-space:nowrap}
  .headline{left:40px;width:320px;top:160px;text-align:center;color:var(--brand-blue);
    font-size:34px;font-weight:700;line-height:40px;letter-spacing:.5px}
  .bar{height:27px;background:var(--bar-blue);border-radius:0 14px 14px 0;
    color:var(--label-yellow);font-size:16px;font-weight:600;line-height:27px;padding-left:22px;text-transform:uppercase;white-space:nowrap}
  .bar.right{border-radius:14px;padding-left:56px}
  .bullets{list-style:none;font-size:13.5px;line-height:16px;color:var(--magenta);font-weight:600;white-space:nowrap}
  .bullets li::before{content:"•";margin-right:6px;font-size:11px}
  .sub{font-size:15.5px;font-weight:600;text-transform:uppercase;line-height:18px;white-space:nowrap}
  .copy{font-size:12.5px;line-height:16px}
  .phone{left:1094px;top:31px;display:flex;align-items:center;gap:8px}
  .phone-badge{width:45px;height:45px;flex:none}
  .phone-number{background:var(--red);color:#fff;font-family:"Oswald",sans-serif;font-weight:600;
    font-size:21px;height:45px;line-height:45px;padding:0 9px;letter-spacing:0;white-space:nowrap;flex:none}
  .estimate{left:1140px;width:180px;top:82px;text-align:center;color:var(--red);font-size:13px;line-height:18px}
  .estimate strong{font-size:15.5px;font-weight:400}
  .claims{left:940px;width:380px;top:152px;text-align:center;font-size:18.5px;line-height:29px;text-transform:uppercase}
  .partners{left:990px;width:312px;top:665px;border-top:1.5px solid #8a8a8a}
  .partner-row{position:absolute;display:flex;gap:22px;align-items:center;font-size:13px;font-weight:600;white-space:nowrap}
  .partner-row span:nth-child(1){color:var(--navy)}
  .partner-row.one span:nth-child(2){color:var(--red)}
  .partner-row.one span:nth-child(3){color:var(--magenta)}
  .partner-row.two span{color:var(--brand-blue)}
</style>
</head>
<body>
<div class="spread">
  <svg class="spread-art" viewBox="0 0 1350 800" width="1350" height="800">
    <defs>
      <linearGradient id="panelFade" x1="0" y1="0" x2="0" y2="1">
        <stop offset="0" stop-color="#ffffff"/><stop offset=".25" stop-color="#ffffff"/>
        <stop offset="1" stop-color="#7f9fd6"/>
      </linearGradient>
      <linearGradient id="panelFadeRight" x1="0" y1="0" x2="0" y2="1">
        <stop offset="0" stop-color="#7f9fd6"/><stop offset=".6" stop-color="#ffffff"/>
        <stop offset="1" stop-color="#ffffff"/>
      </linearGradient>
      <linearGradient id="topPhoto" x1="0" y1="0" x2="1" y2="0">
        <stop offset="0" stop-color="#b9bcc0"/><stop offset=".5" stop-color="#d8d4d2"/>
        <stop offset=".55" stop-color="#d03a3a"/><stop offset="1" stop-color="#e8e2e0"/>
      </linearGradient>
      <linearGradient id="wiresPhoto" x1="0" y1="0" x2="1" y2="1">
        <stop offset="0" stop-color="#9fb06a"/><stop offset=".5" stop-color="#d9d36a"/>
        <stop offset="1" stop-color="#e9ecef"/>
      </linearGradient>
      <linearGradient id="climberPhoto" x1="0" y1="0" x2="1" y2="1">
        <stop offset="0" stop-color="#5d7e9c"/><stop offset="1" stop-color="#b9c8d6"/>
      </linearGradient>
      <linearGradient id="rollerPhoto" x1="0" y1="0" x2="1" y2="1">
        <stop offset="0" stop-color="#f2f2f2"/><stop offset="1" stop-color="#dcdcdc"/>
      </linearGradient>
      <clipPath id="leftPanel"><polygon points="0,0 295,0 679,400 270,800 0,800"/></clipPath>
      <clipPath id="rightPanel"><polygon points="1065,0 1350,0 1350,800 1060,800 679,400"/></clipPath>
    </defs>

    <polygon points="0,0 295,0 679,400 270,800 0,800" fill="url(#panelFade)"/>
    <polygon points="1065,0 1350,0 1350,800 1060,800 679,400" fill="url(#panelFadeRight)"/>

    <g role="img" aria-label="Photo of gloved hands cleaning a kitchen counter">
      <polygon points="295,0 1065,0 679,400" fill="url(#topPhoto)"/>
    </g>
    <g role="img" aria-label="Photo of an electrician working on a wiring panel">
      <polygon points="270,800 1060,800 679,400" fill="url(#wiresPhoto)"/>
    </g>
    <g clip-path="url(#leftPanel)">
      <g role="img" aria-label="Photo of a rope-access worker cleaning building windows">
        <circle cx="582" cy="402" r="222" fill="url(#climberPhoto)"/>
      </g>
      <circle cx="582" cy="402" r="229" fill="none" stroke="var(--magenta)" stroke-width="11"/>
    </g>
    <g clip-path="url(#rightPanel)">
      <g role="img" aria-label="Photo of a paint roller on a white wall">
        <circle cx="778" cy="402" r="222" fill="url(#rollerPhoto)"/>
      </g>
      <circle cx="778" cy="402" r="229" fill="none" stroke="var(--magenta)" stroke-width="11"/>
    </g>
    <g stroke="#ffffff" stroke-width="8" fill="none">
      <polyline points="295,0 679,400 270,800"/>
      <polyline points="1065,0 679,400 1060,800"/>
    </g>
  </svg>

  <div class="abs brand"><span class="brand-mark"></span><span class="brand-name">QNV Cleaning</span></div>
  <h1 class="abs headline">YOUR PROPERTY,<br>OUR PRIORITY.</h1>

  <div class="abs bar" style="left:68px;top:270px;width:312px">Cleaning Services:</div>
  <ul class="abs bullets" style="left:90px;top:300px">
    <li>Building Cleaning</li><li>House Cleaning</li><li>Office Cleaning</li>
  </ul>
  <div class="abs sub" style="left:90px;top:368px">Hassle Free Rate</div>
  <p class="abs copy" style="left:90px;top:387px;width:250px">Your home, your services, your priorities. We specialize in kitchens, bathrooms, floors and dusting, and on every cleaning services, we’ll make sure that those areas shine..</p>

  <div class="abs bar" style="left:68px;top:473px;width:300px">Housekeeping Training:</div>
  <ul class="abs bullets" style="left:90px;top:503px">
    <li>Essentials of Housekeeping</li><li>Good Manners and Serving Etiquitte</li><li>Housekeeping for Hotels</li>
  </ul>
  <div class="abs sub" style="left:90px;top:573px">Temporary Part-Time Maids</div>
  <p class="abs copy" style="left:90px;top:592px;width:262px">Foreign domestic helper away? Need short-term house cleaning help? Sprucing up a new apartment or a vacant one can be an unfamiliar task and ignite a feeling of frustration. Relieve your burden and leave it in the hands of our efficient team who will ensure that it is spick and span in no time! We do provide temporary part-time helpers to assist you in house cleaning.</p>

  <div class="abs phone">
    <svg class="phone-badge" viewBox="0 0 45 45">
      <circle cx="22.5" cy="22.5" r="20" fill="#fff" stroke="var(--red)" stroke-width="3"/>
      <path d="M15 13c2-2 4 2 5 4s-2 3-1 5 3 4 5 5 3-2 5-1 5 3 3 5-4 3-7 1-10-7-11-11 0-6 1-8z" fill="var(--red)"/>
    </svg>
    <div class="phone-number">800 PRIMECARE</div>
  </div>
  <p class="abs estimate">Call us now for a<br><strong>FREE ESTIMATE</strong></p>
  <p class="abs claims">European Managed<br>Annual Maintenance Contracts<br>On Call Service</p>

  <div class="abs bar right" style="left:984px;top:282px;width:304px">Property Maintenance:</div>
  <ul class="abs bullets" style="left:1040px;top:312px">
    <li>AC Services</li><li>Plumbing Services</li><li>Electrical Services</li><li>Handyman Services</li>
  </ul>
  <p class="abs copy" style="left:1040px;top:399px;width:250px">Hurra Mendo is reinventing the maintenance industry in Dubai with GPS technology and world class inventory management.</p>
  <p class="abs copy" style="left:1040px;top:463px;width:250px">This means you get the right technician, with the right tools at the right time!</p>

  <div class="abs bar right" style="left:984px;top:522px;width:304px">Pest Control Services:</div>
  <ul class="abs bullets" style="left:1040px;top:552px">
    <li>General pest control</li><li>Bed bugs control</li><li>Rat control</li><li>Cockroaches control</li><li>Ant control</li>
  </ul>

  <div class="abs partners">
    <div class="partner-row one" style="left:30px;top:22px"><span>QNV Pest Control</span><span>KRV Works</span><span>HelperList</span></div>
    <div class="partner-row two" style="left:115px;top:72px"><span>Hurra Mendo</span><span>Tawrid</span><span>Aquela</span></div>
  </div>
</div>
</body>
</html>
```